Ridgeway Ore Advisory Business Card

Ridgeway Ore Advisory is a company that provides consulting services to the Mining Industry.

Whilst Ridgeway Ore Advisory is an Australian based company its client base is the global mining industry.

The essence of Ridgeway Ore Advisory is its a can do organisation that can make a difference to its clients by providing quality assistance and form lasting relationships.
Updates

Target Market(s)

The global Mining Industry.

Industry/Entity Type

Mining

Font styles to use
Serif

Colors

Designer to choose colors to be used in the design.

Requirements
Nice to have
• My thinking is the card would look good in black given the logo.

I would like to see written on the back side of the card " Providing Metallurgical, Management and Corporate Services to the Mining Industry"

```html
<!DOCTYPE html>
<html lang="en">
<head>
<meta charset="utf-8">
<title>Ridgeway Ore Advisory – Business Card</title>
<link rel="stylesheet" href="https://fonts.googleapis.com/css2?family=Raleway:wght@300;800&family=Roboto:wght@400;700&display=swap">
<style>
  :root {
    --backdrop: #e4e5e7;
    --card-white: #ffffff;
    --card-black: #000000;
    --ink: #111111;
    --ore-orange: #f6a31c;
    --divider: #111111;
  }
  html, body {
    margin: 0;
    padding: 0;
    width: 1200px;
    height: 1200px;
    overflow: hidden;
    background: var(--backdrop);
  }
  .canvas {
    position: relative;
    width: 1200px;
    height: 1200px;
  }
  .card {
    position: absolute;
    left: 174px;
    width: 852px;
    height: 488px;
    overflow: hidden;
  }
  .card--front { top: 69px; background: var(--card-white); }
  .card--back  { top: 643px; background: var(--card-black); }

  .wordmark {
    position: absolute;
    margin: 0;
    font-family: "Roboto", Arial, sans-serif;
    font-weight: 700;
    color: var(--ore-orange);
    line-height: 1.05;
    letter-spacing: 0.5px;
  }
  .card--front .wordmark {
    left: 47px;
    top: 150px;
    width: 360px;
    font-size: 44px;
  }
  .card--back .wordmark {
    left: 0;
    right: 0;
    top: 150px;
    text-align: center;
    font-size: 52px;
  }

  .divider {
    position: absolute;
    left: 434px;
    top: 183px;
    width: 3px;
    height: 305px;
    background: var(--divider);
  }

  .person {
    position: absolute;
    left: 468px;
    top: 168px;
    margin: 0;
    color: var(--ink);
  }
  .person__name {
    display: block;
    font-family: "Raleway", Arial, sans-serif;
    font-weight: 300;
    font-size: 49px;
    line-height: 56px;
  }
  .person__title {
    display: block;
    font-family: "Raleway", Arial, sans-serif;
    font-weight: 800;
    font-size: 24px;
    letter-spacing: 6px;
    line-height: 28px;
  }

  .contact {
    position: absolute;
    left: 468px;
    top: 300px;
    margin: 0;
    font-style: normal;
    font-family: "Roboto", Arial, sans-serif;
    font-size: 23px;
    line-height: 32.5px;
    color: var(--ink);
    letter-spacing: 0.3px;
  }

  .tagline {
    position: absolute;
    left: 0;
    right: 0;
    top: 381px;
    margin: 0;
    text-align: center;
    font-family: "Roboto", Arial, sans-serif;
    font-size: 25px;
    line-height: 32.5px;
    color: var(--ore-orange);
  }
</style>
</head>
<body>
<main class="canvas">
  <section class="card card--front" aria-label="Business card front">
    <p class="wordmark">Ridgeway<br>Ore Advisory</p>
    <div class="divider"></div>
    <h1 class="person">
      <span class="person__name">Daniel Hart</span>
      <span class="person__title">PRESIDENT</span>
    </h1>
    <address class="contact">
      1175 Copperstone Road<br>
      Ashford, NJ 07410<br>
      000-555-0142<br>
      www.RidgewayOA.com<br>
      DanielHart@RidgewayOA.com
    </address>
  </section>

  <section class="card card--back" aria-label="Business card back">
    <p class="wordmark">Ridgeway<br>Ore Advisory</p>
    <p class="tagline">Providing Metallurgical, Management and<br>Corporate Services to the Mining Industry</p>
  </section>
</main>
</body>
</html>
```